Seventy Crumbs needs a business card

Seventy Crumbs needs an attractive, playful, and exciting business card design to attract potential buyers. I have included our logo, label, and social media design files along with the fonts and colors for ideas. For the logo file, please only pay attention to the purple background with white text. I want a card with premium matte and metallic finish. I want my name included, e-mail, and phone number. The logo must be included, and then use the label design and social media design files to add creativity to the design. Only the fonts that are provided should be used as well.

Name: Gregory Talliston
Phone: 555-417-2086
E-mail: gtalliston@seventycrumbs.example

Contact Information for Business Card

I want a card with premium matte and metallic finish. I want my name included, e-mail, and phone number. The logo must be included, and then use the label design and social media design files to add creativity to the design. Only the fonts that are provided should be used as well.

Name: Gregory Talliston
Phone: 555-417-2086

Colors
6b449b

Requirements
Must have
• My logo, my fonts, my colors, my designs to some degree, and my character

```html
<!DOCTYPE html>
<html lang="en">
<head>
<meta charset="utf-8">
<title>Seventy Crumbs — Business Card</title>
<link rel="stylesheet" href="https://fonts.googleapis.com/css2?family=Lato:wght@400;700&family=Great+Vibes&display=swap">
<style>
  :root {
    --backdrop: #9a9a9a;
    --card-purple: #6a459e;
    --card-shadow: rgba(0, 0, 0, 0.35);
    --ink-white: #ffffff;
    --art-turban: #f1eef0;
    --art-skin: #e6b48c;
    --art-vest: #3552a8;
    --art-moon: #f6efa8;
    --star-gold: #f5d34a;
    --star-mauve: #b08a9a;
  }
  * { margin: 0; padding: 0; box-sizing: border-box; }
  html, body { width: 1200px; height: 900px; overflow: hidden; }
  body { background: var(--backdrop); position: relative; font-family: "Lato", sans-serif; }

  .card {
    position: absolute;
    top: 306px;
    width: 439px;
    height: 272px;
    background: var(--card-purple);
    border-radius: 10px;
    box-shadow: 2px 3px 4px var(--card-shadow);
    overflow: hidden;
    color: var(--ink-white);
  }
  .card--front { left: 150px; }
  .card--back { left: 609px; }

  .star-field { position: absolute; inset: 0; width: 439px; height: 272px; }

  .night-sky-art {
    position: absolute;
    left: 150px; top: 10px;
    width: 115px; height: 125px;
    border-radius: 40% 50% 50% 40%;
    background: radial-gradient(ellipse at 45% 30%, rgba(246, 239, 168, 0.75) 0%, rgba(246, 239, 168, 0.3) 28%, rgba(245, 211, 74, 0.12) 55%, rgba(106, 69, 158, 0) 75%);
  }

  .character-art {
    position: absolute;
    left: 0; top: 52px;
    width: 158px; height: 220px;
    border-radius: 70px 70px 0 0;
    background: linear-gradient(180deg, var(--art-turban) 0%, #ecd9cc 30%, var(--art-skin) 48%, #9a85a6 72%, var(--art-vest) 100%);
  }

  .brand-mark {
    position: absolute;
    display: flex;
    align-items: center;
    gap: 8px;
    font-family: "Lato", sans-serif;
    font-weight: 700;
    color: var(--ink-white);
    white-space: nowrap;
  }
  .brand-mark__dot { border-radius: 50%; background: var(--ink-white); flex: none; }
  .card--front .brand-mark { right: 22px; top: 62px; font-size: 19px; }
  .card--front .brand-mark__dot { width: 12px; height: 12px; }
  .card--back .brand-mark { left: 50%; top: 50%; transform: translate(-50%, -50%); font-size: 32px; }
  .card--back .brand-mark__dot { width: 20px; height: 20px; }

  .holder-name {
    position: absolute;
    left: 166px; top: 162px;
    font-family: "Great Vibes", cursive;
    font-size: 31px;
    font-weight: 400;
    line-height: 1;
    white-space: nowrap;
  }
  .contact-list {
    position: absolute;
    left: 172px; top: 207px;
    list-style: none;
    font-size: 14.5px;
    line-height: 23px;
    white-space: nowrap;
  }
</style>
</head>
<body>
  <section class="card card--front" aria-label="Business card front">
    <svg class="star-field" viewBox="0 0 439 272" aria-hidden="true">
      <g fill="var(--star-gold)">
        <circle cx="40" cy="34" r="2"/>
        <circle cx="58" cy="22" r="1.5"/>
        <circle cx="96" cy="18" r="1.5"/>
        <circle cx="122" cy="20" r="1.5"/>
        <circle cx="12" cy="30" r="1.2"/>
        <circle cx="150" cy="40" r="1.5"/>
      </g>
      <g fill="var(--star-mauve)">
        <circle cx="66" cy="30" r="2.5"/>
        <circle cx="140" cy="64" r="3"/>
        <circle cx="296" cy="36" r="2.5"/>
      </g>
    </svg>
    <div class="night-sky-art" role="img" aria-label="Crescent moon with a trail of golden sparkles"></div>
    <div class="character-art" role="img" aria-label="Cartoon character in a white turban and blue vest pointing upward"></div>
    <div class="brand-mark"><span class="brand-mark__dot"></span><span>Seventy Crumbs</span></div>
    <h1 class="holder-name">Gregory Talliston</h1>
    <ul class="contact-list">
      <li>P: 555-417-2086</li>
      <li>E: gtalliston@seventycrumbs.example</li>
    </ul>
  </section>

  <section class="card card--back" aria-label="Business card back">
    <div class="brand-mark"><span class="brand-mark__dot"></span><span>Seventy Crumbs</span></div>
  </section>
</body>
</html>
```